Greeting Card Design Project

We need a greeting card to email our clients during christmas.

We are suppliers for cutting tools & machine accessories. You can find out more about us at our website www.quvantel.com.sg

Reason: I've decide to extend the deadline as I'm awaiting more designs, thank you.

```html
<!DOCTYPE html>
<html lang="en">
<head>
<meta charset="utf-8">
<title>Happy Christmas – Quvantel Tools</title>
<link href="https://fonts.googleapis.com/css2?family=Indie+Flower&display=swap" rel="stylesheet">
<style>
  :root {
    --paper: #ffffff;
    --edge: #d9d4d6;
    --festive-red: #e8231f;
    --warm-red: #f4452a;
    --maroon: #9e1a3c;
    --orange: #f39a1c;
    --steel: #9aa3a6;
    --gear-white: #f1f3ee;
    --brand-maroon: #8a1838;
  }
  html, body {
    margin: 0;
    padding: 0;
    width: 1200px;
    height: 857px;
    overflow: hidden;
    background: var(--paper);
  }
  .greeting-card {
    position: relative;
    width: 1200px;
    height: 857px;
    box-sizing: border-box;
    border: 1px solid var(--edge);
    background: var(--paper);
    font-family: "Indie Flower", cursive;
    overflow: hidden;
  }
  .card-title {
    position: absolute;
    top: 26px;
    left: 0;
    width: 100%;
    margin: 0;
    text-align: center;
    font-weight: 400;
    font-size: 70px;
    line-height: 1;
    color: var(--festive-red);
    letter-spacing: 2px;
  }
  .card-wish {
    position: absolute;
    top: 108px;
    left: 190px;
    margin: 0;
    font-size: 38px;
    line-height: 1;
    letter-spacing: 1px;
    color: var(--festive-red);
    white-space: nowrap;
  }
  .card-year {
    font-size: 58px;
    margin-left: 18px;
    vertical-align: -6px;
  }
  .gear-band {
    position: absolute;
    top: 180px;
    left: 0;
    width: 1200px;
    height: 535px;
    background:
      radial-gradient(circle at 38% 62%, rgba(241, 243, 238, 0.55) 0, rgba(241, 243, 238, 0.35) 18%, transparent 30%),
      radial-gradient(circle at 63% 30%, rgba(241, 243, 238, 0.5) 0, rgba(241, 243, 238, 0.3) 14%, transparent 24%),
      radial-gradient(circle at 12% 55%, rgba(158, 26, 60, 0.75), transparent 22%),
      radial-gradient(circle at 33% 20%, rgba(158, 26, 60, 0.6), transparent 18%),
      radial-gradient(circle at 97% 45%, rgba(158, 26, 60, 0.7), transparent 16%),
      radial-gradient(circle at 72% 55%, rgba(158, 26, 60, 0.45), transparent 22%),
      radial-gradient(circle at 76% 48%, rgba(243, 154, 28, 0.55), transparent 8%),
      radial-gradient(circle at 11% 8%, rgba(243, 154, 28, 0.5), transparent 6%),
      radial-gradient(circle at 89% 82%, rgba(243, 154, 28, 0.45), transparent 6%),
      radial-gradient(circle at 48% 12%, rgba(154, 163, 166, 0.5), transparent 5%),
      radial-gradient(circle at 2% 12%, rgba(154, 163, 166, 0.5), transparent 5%),
      linear-gradient(90deg, var(--festive-red), var(--warm-red) 50%, var(--festive-red));
  }
  .brand {
    position: absolute;
    right: 40px;
    bottom: 58px;
    display: flex;
    align-items: center;
    gap: 12px;
    color: var(--brand-maroon);
    font-size: 42px;
    line-height: 1;
    letter-spacing: 1px;
    text-transform: uppercase;
  }
  .brand-dot {
    width: 26px;
    height: 26px;
    border-radius: 50%;
    background: var(--brand-maroon);
  }
</style>
</head>
<body>
  <main class="greeting-card">
    <h1 class="card-title">Happy Christmas...</h1>
    <p class="card-wish">We wish you a Healthy &amp; Prosperous<span class="card-year">2013</span></p>
    <div class="gear-band" role="img" aria-label="Red band patterned with interlocking gears in maroon, orange and grey, with two large white gears in front"></div>
    <div class="brand">
      <span class="brand-dot"></span>
      <span class="brand-name">Quvantel Tools</span>
    </div>
  </main>
</body>
</html>
```